Design for 3.31” x 84” vinyl banner for tradeshow

Hello, I am looking for a design that will be printed on a 33.31” x 84” vinyl banner for my company’s tradeshow booth.

-Design

My vision: I want to give you the full background, because I think it’ll help. We design insulation for electronic tools that go in high temperature oilwells. Interestingly, a lot of the electronic tools that go down these oil wells are also used in geothermal wells. However the electronics would melt in these high temperature geothermal wells if they were not insulated. A lot of companies that make tools for the oil market are trying to re-purpose their existing tools for the geothermal market…..and to do this, they would need our insulation.

So, our sign needs to conveys this message: Trying to enter the geothermal logging market? it's as simple as increasing the temp. rating for your existing tools

This sign will be placed at our company’s booth at an industry tradeshow. The sign needs to have a similar style to our existing signs. I’ve included images of our booth and all of our other signs. This sign doesn’t have to be identical in artistic style, but be fairly similar.

-Art Requirements:

At least 1 Image of RDP logo

I’ve included several different variations. Use your judgement to select the one that you think is most fitting.

Do not use the portion of the logo that says “40 years”. Feel free to crop that out if you would like.

At least 2 images of logging tools. You can select more than 2 if you think that’s necessary. Logging tools are the long metal tubes.

I’ve included several pictures of different logging tools. I would like to see at least 2 pictures of tools on the banner. Please include the image titled “Full, double centarlizer” It could look cool if this picture extended the full length of the banner (just a suggestion). I purchased these images off of picvault.For the second image of the tool, feel free to include whatever tool you think looks best.

-Colors and font: Like I mentioned above, I would like it to look close to the other signs we have at our booth. Please select colors and fonts that will fit with our other signs.

-Other thoughts/suggestions

When most people in our industry think of geothermal, the automatically associate it with extremely high temperatures. I’m open to seeing warmer colors (orange/red) that help convey this idea.

I’m also open to seeing pictures of geothermal power plants, I included an image of this titled “geothermal” that you may use if you like. This is not mandatory, just a suggestion.

-Text: the main text needs to be: “Trying to enter the Geothermal logging market? Ask us about increasing the temperature rating for your existing tools” No other text is required.

Printing/Art specifications:

I’ll be giving the design I receive off art-hive to a local banner printing shop. I’ve included their printing and art guidelines, please take a look at it and let me know if you have any questions. It’s pretty detailed so I hope it provides you with enough information. The design would have to follow the requirements in the two attached word documents.

Target Market(s)

oil and gas professionals

Industry/Entity Type

oil and gas/geothermal

Font styles to use
Other font styles liked:
• Fonts similar the font used on our other tradeshow signs (images attached)

Colors
F0912C
F2A743
F7CA91
FBE8D2
FDF5EE

Requirements
Must have
• -At least 1 Image of RDP logo, At least 2 images of logging tools (1 of these 2 pictures must be image titled "full double centralizer", he main text needs to be: “Trying to enter the Geothermal logging market? Ask us about increasing the temperature rating for your existing tools” , the design must follow the requirements in the printing and art guideline documents I attached.
Nice to have
• please select colors and fonts that will fit with our other signs.

```html
<!DOCTYPE html>
<html lang="en">
<head>
<meta charset="utf-8">
<title>Redpoint Downhole – Geothermal Banner</title>
<link rel="stylesheet" href="https://fonts.googleapis.com/css2?family=Montserrat:wght@400;700;800;900&display=swap">
<style>
  :root {
    --stage: #e6e6e6;
    --ink: #0a0a0a;
    --ink-soft: #161616;
    --orange: #ff7f00;
    --white: #ffffff;
    --rule: #5a5a5a;
    --text-soft: #f2f2f2;
    --pattern-tone: #3a2f1c;
    --steel-dark: #3c3c40;
    --steel: #8a8a90;
    --steel-light: #b9b9bf;
    --copper: #8a5a3a;
  }
  * { box-sizing: border-box; margin: 0; padding: 0; }
  html, body {
    width: 686px; height: 1200px; overflow: hidden;
    background: var(--stage);
    font-family: "Montserrat", Arial, sans-serif;
  }
  .banner {
    position: absolute; left: 104px; top: 0;
    width: 478px; height: 1200px;
    background: linear-gradient(180deg, var(--ink-soft) 0%, var(--ink) 22%, var(--ink) 100%);
    color: var(--white);
    overflow: hidden;
  }
  .pattern-field {
    position: absolute; inset: 0;
    background:
      radial-gradient(ellipse 38% 22% at 6% 4%, rgba(110, 86, 48, 0.55) 0%, rgba(58, 47, 28, 0) 100%),
      radial-gradient(ellipse 38% 22% at 94% 4%, rgba(110, 86, 48, 0.5) 0%, rgba(58, 47, 28, 0) 100%),
      radial-gradient(ellipse 30% 30% at 0% 72%, rgba(70, 56, 34, 0.35) 0%, rgba(58, 47, 28, 0) 100%),
      radial-gradient(ellipse 30% 30% at 100% 72%, rgba(70, 56, 34, 0.35) 0%, rgba(58, 47, 28, 0) 100%);
  }
  .brand {
    position: absolute; top: 81px; left: 0; width: 100%;
    display: flex; align-items: center; justify-content: center; gap: 10px;
  }
  .brand-square {
    width: 78px; height: 78px; background: var(--white); border-radius: 4px;
  }
  .brand-name {
    font-weight: 800; font-size: 23px; line-height: 1.2;
    color: var(--white); letter-spacing: 0.3px;
  }
  .headline {
    position: absolute; top: 214px; left: 0; width: 100%;
    text-align: center; font-weight: 800; line-height: 1;
  }
  .headline .lead { display: block; font-size: 37px; letter-spacing: 0.2px; }
  .headline .accent { display: block; font-size: 51px; color: var(--orange); margin-top: 2px; letter-spacing: -0.5px; }
  .headline .tail { display: block; font-size: 43px; margin-top: -3px; }
  .divider {
    position: absolute; top: 373px; left: 51px; width: 376px; height: 1px;
    background: var(--rule);
  }
  .divider::after {
    content: ""; position: absolute; left: 50%; top: -2px;
    width: 84px; height: 5px; margin-left: -42px;
    background: var(--orange); border-radius: 3px;
  }
  .subline {
    position: absolute; top: 399px; left: 0; width: 100%;
    text-align: center; font-weight: 400; font-size: 21px;
    line-height: 23px; letter-spacing: 1.2px; color: var(--text-soft);
  }
  .tools-photo {
    position: absolute; top: 486px; left: 0; width: 100%; height: 650px;
    background:
      linear-gradient(180deg, rgba(10,10,10,0.85) 0%, rgba(10,10,10,0) 12%, rgba(10,10,10,0) 88%, rgba(10,10,10,0.6) 100%),
      linear-gradient(90deg,
        #0c0c0c 0%, #0c0c0c 10%,
        var(--steel-dark) 13%, var(--steel) 16%, var(--copper) 17.5%, var(--steel-dark) 20%,
        #111 26%, var(--steel-dark) 29%, var(--steel) 30.5%, var(--steel-dark) 32%, #141414 37%,
        #242424 44%, var(--steel-light) 49%, var(--copper) 50%, var(--steel-light) 51%, #242424 56%,
        #141414 63%, var(--steel-dark) 68%, var(--steel) 69.5%, var(--steel-dark) 71%, #111 74%,
        var(--steel-dark) 80%, var(--steel) 83%, var(--copper) 84.5%, var(--steel-dark) 87%,
        #0c0c0c 90%, #0c0c0c 100%);
    opacity: 0.9;
  }
  .footer-band {
    position: absolute; left: 0; bottom: 0; width: 478px; height: 82px;
  }
  .footer-url {
    position: absolute; left: 0; bottom: 29px; width: 100%;
    text-align: center; font-weight: 700; font-size: 17px;
    letter-spacing: 0.8px; color: var(--white);
  }
</style>
</head>
<body>
  <main class="banner">
    <div class="pattern-field" role="img" aria-label="Faint gold triangle lattice across the dark background"></div>

    <header class="brand">
      <span class="brand-square" aria-hidden="true"></span>
      <span class="brand-name">REDPOINT<br>DOWNHOLE, Inc.</span>
    </header>

    <h1 class="headline">
      <span class="lead">Trying to enter the</span>
      <span class="accent">GEOTHERMAL</span>
      <span class="tail">logging market?</span>
    </h1>

    <div class="divider" aria-hidden="true"></div>

    <p class="subline">Ask us about increasing<br>the temperature rating<br>for your existing tools</p>

    <div class="tools-photo" role="img" aria-label="Five metal logging tools with centralizer arms standing in front of a dim drilling rig"></div>

    <svg class="footer-band" viewBox="0 0 478 82" aria-hidden="true">
      <rect x="0" y="0" width="478" height="82" fill="var(--orange)"/>
      <path d="M0 0 H34 C56 0 62 12 68 28 C76 48 84 60 106 60 H372 C394 60 402 48 410 28 C416 12 422 0 444 0 H478 V-2 H0 Z" fill="var(--ink)"/>
    </svg>
    <p class="footer-url">www.redpointdownhole.com</p>
  </main>
</body>
</html>
```